Brightwell Holdings -Business Card Design Project

I have a new logo to put onto business cards - attached
The word doc shows how I want it all laid out - front page and rear
The lettering I want is clean and rounded - modern
Updates
Project Deadline Extended
Reason: There was no original deadline!
Target Market(s)
25-49 year old leaders and entrepreneurs in Australia
Industry/Entity Type
Business

```html
<!DOCTYPE html>
<html lang="en">
<head>
<meta charset="utf-8">
<title>Brightwell Holdings – Business Cards</title>
<link rel="stylesheet" href="https://fonts.googleapis.com/css2?family=Open+Sans:wght@400;600;700&display=swap">
<style>
  :root {
    --brand-blue: #0d4f9c;
    --ink: #333333;
    --soft-grey: #a9a9a9;
    --icon-border: #2b2b2b;
    --card: #ffffff;
    --backdrop: #e9e7e3;
  }
  * { margin: 0; padding: 0; box-sizing: border-box; }
  html, body {
    width: 1200px; height: 1166px; overflow: hidden;
    background: var(--backdrop);
    font-family: "Open Sans", Arial, sans-serif;
    color: var(--ink);
  }
  .canvas { position: relative; width: 1200px; height: 1166px; }
  .card {
    position: absolute; background: var(--card);
    width: 543px; height: 315px;
    box-shadow: 0 6px 24px rgba(0,0,0,0.12);
    overflow: hidden;
  }
  /* Back side: contacts */
  .card--back { left: 140px; top: 210px; }
  .contact {
    position: absolute; top: 101px; width: 200px; text-align: center;
    font-size: 14px; white-space: nowrap;
  }
  .contact__icon {
    width: 76px; height: 76px; margin: 0 auto 21px;
    border: 3px solid var(--icon-border);
    display: flex; align-items: center; justify-content: center;
  }
  .contact__icon--blue { background: var(--brand-blue); }
  .contact__icon--grey { background: var(--soft-grey); }
  .contact--phone { left: 10px; }
  .contact--email { left: 172px; }
  .contact--web { left: 332px; }
  .address-band { position: absolute; left: 0; bottom: 0; width: 467px; height: 42px; }
  .address {
    position: absolute; left: 118px; bottom: 0; height: 42px;
    display: flex; align-items: center; gap: 10px;
    color: #fff; font-size: 15px; white-space: nowrap;
  }
  /* Front side: identity */
  .card--front { left: 517px; top: 666px; }
  .accent-squares { position: absolute; left: 28px; top: 32px; display: flex; gap: 19px; }
  .accent-squares span { width: 14px; height: 14px; background: var(--brand-blue); }
  .accent-squares span:nth-child(2) { background: var(--ink); }
  .brand {
    position: absolute; left: 48px; top: 178px;
    display: flex; align-items: center; gap: 10px;
    color: var(--brand-blue); font-weight: 600; font-size: 19px; letter-spacing: 0.5px;
    white-space: nowrap;
  }
  .brand__mark { width: 26px; height: 26px; background: var(--brand-blue); }
  .person { position: absolute; right: 53px; top: 190px; text-align: right; white-space: nowrap; }
  .person__name { font-weight: 700; font-size: 31px; line-height: 1.1; }
  .person__role { font-size: 23px; margin-top: 8px; }
  .divider { position: absolute; left: 0; top: 251px; width: 383px; height: 4px; display: flex; }
  .divider span { height: 4px; }
  .divider .seg-a { width: 106px; background: var(--brand-blue); }
  .divider .seg-b { width: 144px; background: var(--ink); }
  .divider .seg-c { width: 133px; background: var(--brand-blue); }
</style>
</head>
<body>
<div class="canvas">

  <section class="card card--back">
    <div class="contact contact--phone">
      <div class="contact__icon contact__icon--blue">
        <svg width="24" height="36" viewBox="0 0 24 36"><rect x="2" y="1" width="20" height="34" rx="3" fill="#fff"/><rect x="5" y="5" width="14" height="22" fill="#0d4f9c"/><circle cx="12" cy="31" r="2" fill="#0d4f9c"/></svg>
      </div>
      02 9555 0147
    </div>
    <div class="contact contact--email">
      <div class="contact__icon contact__icon--grey">
        <svg width="30" height="22" viewBox="0 0 30 22"><rect x="1" y="1" width="28" height="20" fill="#fff"/><path d="M1 1 L15 12 L29 1" fill="none" stroke="#a9a9a9" stroke-width="2"/></svg>
      </div>
      hello@brightwell.au
    </div>
    <div class="contact contact--web">
      <div class="contact__icon contact__icon--blue">
        <svg width="32" height="32" viewBox="0 0 32 32" fill="none" stroke="#fff" stroke-width="2"><circle cx="16" cy="16" r="13"/><ellipse cx="16" cy="16" rx="6" ry="13"/><line x1="3" y1="16" x2="29" y2="16"/><line x1="5" y1="9" x2="27" y2="9"/><line x1="5" y1="23" x2="27" y2="23"/></svg>
      </div>
      brightwell.au
    </div>
    <svg class="address-band" viewBox="0 0 467 42" preserveAspectRatio="none"><polygon points="0,0 423,0 467,42 0,42" fill="#0d4f9c"/></svg>
    <div class="address">
      <svg width="13" height="19" viewBox="0 0 13 19"><path d="M6.5 0C2.9 0 0 2.9 0 6.5 0 11 6.5 19 6.5 19S13 11 13 6.5C13 2.9 10.1 0 6.5 0z" fill="#fff"/><circle cx="6.5" cy="6.5" r="2.5" fill="#0d4f9c"/></svg>
      27 Harbour Lane Seaview, NSW 2099
    </div>
  </section>

  <section class="card card--front">
    <div class="accent-squares"><span></span><span></span><span></span></div>
    <div class="brand"><span class="brand__mark"></span>Brightwell Holdings</div>
    <div class="person">
      <div class="person__name">Daniel Hart</div>
      <div class="person__role">Founder</div>
    </div>
    <div class="divider"><span class="seg-a"></span><span class="seg-b"></span><span class="seg-c"></span></div>
  </section>

</div>
</body>
</html>
```